I would like a formal monogram with LM and Lorna Mabbery Interiors written somehow. this a a new interior design company based in Dallas. My favorite colors is Halvorne blue with gold or white writing or some variation of.
back: Lorna Mabbery
214-630-4182
lorna.mabbery@quillpost.example
www.lornamabberyinteriors.example

```html
<!DOCTYPE html>
<html lang="en">
<head>
<meta charset="utf-8">
<title>Lorna Mabbery Interiors – Business Card</title>
<link rel="stylesheet" href="https://fonts.googleapis.com/css2?family=Red+Hat+Display:wght@500&family=Josefin+Sans:wght@400&family=Cormorant+Garamond:wght@500&family=Poppins:wght@400;500&display=swap">
<style>
  :root {
    --backdrop: #222828;
    --card: #0b1715;
    --card-edge: #13221f;
    --gold: #e6b43c;
    --gold-light: #f6d569;
    --gold-deep: #d39a2a;
    --white: #f4f4f2;
    --heading: #ffffff;
  }
  * { margin: 0; padding: 0; box-sizing: border-box; }
  html, body {
    width: 1200px; height: 971px; overflow: hidden;
    background: radial-gradient(ellipse at 50% 45%, #2a3030 0%, var(--backdrop) 70%);
  }
  .canvas { position: relative; width: 1200px; height: 971px; }

  .presentation-title {
    position: absolute; left: 748px; top: 22px;
    font-family: "Red Hat Display", sans-serif; font-weight: 500;
    color: var(--heading); font-size: 34px; letter-spacing: -0.3px;
  }
  .presentation-size {
    position: absolute; left: 750px; top: 70px;
    font-family: "Red Hat Display", sans-serif; font-weight: 500;
    color: var(--heading); font-size: 25px;
  }

  .card {
    position: absolute; width: 560px; height: 320px;
    background: var(--card); border-radius: 22px;
    border: 1px solid var(--card-edge);
    box-shadow: 0 24px 50px rgba(0,0,0,.55);
    overflow: hidden;
  }
  .card--front { left: 70px; top: 190px; }
  .card--back { left: 570px; top: 540px; }

  /* front */
  .brand-mark {
    position: absolute; left: 50%; top: 44px; transform: translateX(-50%);
    width: 96px; height: 96px; border-radius: 50%;
    border: 3px solid var(--gold);
  }
  .brand-name {
    position: absolute; left: 0; right: 0; top: 158px; text-align: center;
    font-family: "Josefin Sans", sans-serif; font-weight: 400;
    color: var(--gold); font-size: 34px; letter-spacing: 0.5px;
  }
  .gold-band {
    position: absolute; left: 0; right: 0; top: 222px; height: 28px;
    background: linear-gradient(90deg, var(--gold) 0%, var(--gold-light) 35%, var(--gold-deep) 70%, var(--gold) 100%);
  }

  /* back */
  .holder-name {
    position: absolute; left: 34px; top: 40px;
    font-family: "Cormorant Garamond", serif; font-weight: 500;
    color: var(--gold); font-size: 30px; letter-spacing: 1.5px; text-transform: uppercase;
  }
  .holder-role {
    position: absolute; left: 36px; top: 80px;
    font-family: "Poppins", sans-serif; font-weight: 500;
    color: var(--white); font-size: 13px;
  }
  .back-brand {
    position: absolute; right: 30px; top: 34px; width: 170px; text-align: center;
  }
  .back-brand .brand-mark-small {
    display: block; margin: 0 auto 10px; width: 70px; height: 70px;
    border-radius: 50%; border: 2px solid var(--gold);
  }
  .back-brand .brand-name-small {
    font-family: "Josefin Sans", sans-serif; font-weight: 400;
    color: var(--gold); font-size: 16px; line-height: 1.25;
  }
  .contact-list {
    position: absolute; left: 36px; bottom: 34px; list-style: none;
    font-family: "Poppins", sans-serif; font-weight: 400;
    color: var(--white); font-size: 13px;
  }
  .contact-list li { display: flex; align-items: center; gap: 10px; height: 24px; }
  .contact-list svg { width: 14px; height: 14px; flex: none; fill: var(--gold); }
</style>
</head>
<body>
<main class="canvas">
  <h1 class="presentation-title">Business Card- Mockup 1</h1>
  <p class="presentation-size">Size: 3.5in X 2.0 in</p>

  <section class="card card--front" aria-label="Card front">
    <span class="brand-mark" aria-hidden="true"></span>
    <p class="brand-name">Lorna Mabbery Interiors</p>
    <div class="gold-band"></div>
  </section>

  <section class="card card--back" aria-label="Card back">
    <h2 class="holder-name">Lorna Mabbery</h2>
    <p class="holder-role">Owner</p>

    <div class="back-brand">
      <span class="brand-mark-small" aria-hidden="true"></span>
      <p class="brand-name-small">Lorna Mabbery Interiors</p>
    </div>

    <ul class="contact-list">
      <li>
        <svg viewBox="0 0 24 24" aria-hidden="true"><path d="M6.6 10.8a15.5 15.5 0 0 0 6.6 6.6l2.2-2.2a1 1 0 0 1 1-.25 11.4 11.4 0 0 0 3.6.57 1 1 0 0 1 1 1V20a1 1 0 0 1-1 1A17 17 0 0 1 3 4a1 1 0 0 1 1-1h3.5a1 1 0 0 1 1 1c0 1.25.2 2.45.57 3.57a1 1 0 0 1-.25 1z"/></svg>
        214-630-4182
      </li>
      <li>
        <svg viewBox="0 0 24 24" aria-hidden="true"><path d="M2 5h20v14H2z M3 6l9 7 9-7" fill="none" stroke="#e6b43c" stroke-width="0"/><path d="M2 5h20v2l-10 7L2 7z"/><path d="M2 9l10 7 10-7v10H2z"/></svg>
        lorna.mabbery@quillpost.example
      </li>
      <li>
        <svg viewBox="0 0 24 24" aria-hidden="true"><path d="M12 2a10 10 0 1 0 0 20 10 10 0 0 0 0-20zm0 2c.9 1.2 1.6 2.9 1.9 5h-3.8c.3-2.1 1-3.8 1.9-5zM4.3 13a8 8 0 0 1 0-2h3.9a18 18 0 0 0 0 2zm.7 2h3.4c.3 1.5.8 2.8 1.4 3.8A8 8 0 0 1 5 15zm3.4-6H5a8 8 0 0 1 4.8-3.8c-.6 1-1.1 2.3-1.4 3.8zM12 20c-.9-1.2-1.6-2.9-1.9-5h3.8c-.3 2.1-1 3.8-1.9 5zm2.1-7H9.9a16 16 0 0 1 0-2h4.2a16 16 0 0 1 0 2zm.1 5.8c.6-1 1.1-2.3 1.4-3.8H19a8 8 0 0 1-4.8 3.8zM15.8 13a18 18 0 0 0 0-2h3.9a8 8 0 0 1 0 2zm-.2-4c-.3-1.5-.8-2.8-1.4-3.8A8 8 0 0 1 19 9z"/></svg>
        www.lornamabberyinteriors.example
      </li>
    </ul>
  </section>
</main>
</body>
</html>
```